Eye catching Stationary Design

Healthcare consultant firm looking for stationary design ( letterhead, envelope and business cards) That’s professional, classy and eye catching . The design should incorporate the logo and the colors of the logo in its design. You can see the logo on our website at www crestmore advisory. net.

```html
<!DOCTYPE html>
<html lang="en">
<head>
<meta charset="utf-8">
<title>Crestmore Advisory – Stationery</title>
<link href="https://fonts.googleapis.com/css2?family=Cinzel:wght@500&family=Open+Sans:wght@400;600;700&display=swap" rel="stylesheet">
<style>
  :root {
    --backdrop: #c4c4c4;
    --paper: #ffffff;
    --navy: #0b56a3;
    --sky: #2ea8d8;
    --bright: #1eaee4;
    --pale: #63c9ef;
    --ink: #2b2b2b;
    --muted: #d9d9d9;
  }
  * { margin: 0; padding: 0; box-sizing: border-box; }
  html, body { width: 1200px; height: 832px; overflow: hidden; background: var(--backdrop); }
  body { position: relative; font-family: "Open Sans", Arial, sans-serif; color: var(--ink); }

  .sheet { position: absolute; background: var(--paper); overflow: hidden; }
  .letterhead { left: 128px; top: 106px; width: 437px; height: 618px; }
  .envelope-back { left: 631px; top: 105px; width: 439px; height: 220px; }
  .envelope-front { left: 631px; top: 341px; width: 439px; height: 219px; }
  .card-front { left: 629px; top: 609px; width: 201px; height: 115px; }
  .card-back { left: 861px; top: 609px; width: 202px; height: 115px; }

  .wordmark {
    position: absolute;
    font-family: "Cinzel", Georgia, serif;
    font-weight: 500;
    color: var(--navy);
    white-space: nowrap;
    transform: translateX(-50%);
    letter-spacing: 0.02em;
  }
  .letterhead .wordmark { left: 50%; top: 62px; font-size: 15px; }
  .envelope-front .wordmark { left: 76px; top: 100px; font-size: 9px; }
  .card-front .wordmark { left: 50%; top: 52px; font-size: 8.5px; }

  .accent-band {
    position: absolute; left: 0; bottom: 0; width: 100%;
    background: linear-gradient(90deg, var(--navy) 0%, var(--bright) 50%, var(--pale) 100%);
  }
  .letterhead .accent-band { height: 52px; }
  .card-front .accent-band { height: 24px; }

  .contact-row {
    position: absolute;
    display: flex;
    justify-content: space-between;
    align-items: flex-start;
    font-size: 4.2px;
    line-height: 1.35;
  }
  .contact-row .item { display: flex; align-items: flex-start; gap: 5px; white-space: nowrap; }
  .contact-row .phone { font-size: 5px; }
  .icon { width: 5px; height: 5px; flex: none; fill: none; stroke: var(--navy); stroke-width: 1.2; }
  .letterhead .contact-row { left: 45px; right: 48px; top: 540px; }
  .envelope-front .contact-row { left: 51px; right: 38px; top: 196px; }

  .envelope-flap { position: absolute; left: 0; top: 0; width: 100%; height: 53px; }
  .window {
    position: absolute; left: 198px; top: 71px; width: 149px; height: 76px;
    border-radius: 6px;
    background: linear-gradient(150deg, #c9c9c9 0%, #d6d6d6 35%, #efefef 50%, #cfcfcf 62%, #d9d9d9 100%);
    box-shadow: inset -2px -2px 4px rgba(0,0,0,0.12);
  }

  .card-back .identity { position: absolute; left: 49px; top: 52px; transform: translateX(-50%); text-align: center; white-space: nowrap; }
  .card-back .name { font-size: 7px; font-weight: 700; color: var(--sky); letter-spacing: 0.06em; }
  .card-back .role { font-size: 5.4px; letter-spacing: 0.04em; color: var(--ink); }
  .card-back .divider { position: absolute; left: 97px; top: 24px; width: 1px; height: 70px; background: linear-gradient(to bottom, transparent, var(--muted), transparent); }
  .card-back .contact-list { position: absolute; left: 111px; top: 30px; list-style: none; font-size: 4px; line-height: 1.3; }
  .card-back .contact-list li { display: flex; gap: 5px; margin-bottom: 7px; white-space: nowrap; }
  .card-back .contact-list .phone { font-size: 5px; }
</style>
</head>
<body>

<svg width="0" height="0" style="position:absolute" aria-hidden="true">
  <defs>
    <symbol id="i-phone" viewBox="0 0 10 10"><path d="M2 1 L4 3 L3 4.5 Q4.5 6.5 5.5 7 L7 6 L9 8 L7.5 9.5 Q3 9 0.5 2.5 Z"/></symbol>
    <symbol id="i-mail" viewBox="0 0 10 10"><rect x="1" y="2.5" width="8" height="5.5"/><path d="M1 2.5 L5 6 L9 2.5"/></symbol>
    <symbol id="i-web" viewBox="0 0 10 10"><circle cx="5" cy="5" r="4"/><path d="M1 5 H9 M5 1 Q2.5 5 5 9 M5 1 Q7.5 5 5 9"/></symbol>
    <symbol id="i-pin" viewBox="0 0 10 10"><path d="M5 9.5 Q1.5 5.5 1.5 3.8 A3.5 3.5 0 0 1 8.5 3.8 Q8.5 5.5 5 9.5 Z"/><circle cx="5" cy="3.8" r="1.2"/></symbol>
  </defs>
</svg>

<section class="sheet letterhead">
  <div class="wordmark">Crestmore Advisory LLC</div>
  <div class="contact-row">
    <span class="item phone"><svg class="icon"><use href="#i-phone"/></svg>(555) 214-0386</span>
    <span class="item"><svg class="icon"><use href="#i-mail"/></svg>info@crestmoreadvisory.net</span>
    <span class="item"><svg class="icon"><use href="#i-web"/></svg>www.crestmoreadvisory.net</span>
    <span class="item"><svg class="icon"><use href="#i-pin"/></svg><span>118 Harbor St Ste 9,<br>Portland, ME 04101, USA</span></span>
  </div>
  <div class="accent-band" role="img" aria-label="Decorative blue wave band along the page foot"></div>
</section>

<section class="sheet envelope-back">
  <svg class="envelope-flap" viewBox="0 0 439 53" preserveAspectRatio="none" aria-hidden="true">
    <path fill="var(--sky)" d="M6 0 H433 L413 46 Q410 52 403 52 H30 Q25 52 22 46 Z"/>
  </svg>
</section>

<section class="sheet envelope-front">
  <div class="wordmark">Crestmore Advisory LLC</div>
  <div class="window"></div>
  <div class="contact-row">
    <span class="item phone"><svg class="icon"><use href="#i-phone"/></svg>(555) 214-0386</span>
    <span class="item"><svg class="icon"><use href="#i-mail"/></svg>info@crestmoreadvisory.net</span>
    <span class="item"><svg class="icon"><use href="#i-web"/></svg>www.crestmoreadvisory.net</span>
    <span class="item"><svg class="icon"><use href="#i-pin"/></svg><span>118 Harbor St Ste 9,<br>Portland, ME 04101, USA</span></span>
  </div>
</section>

<section class="sheet card-front">
  <div class="wordmark">Crestmore Advisory LLC</div>
  <div class="accent-band" role="img" aria-label="Decorative blue wave band along the card foot"></div>
</section>

<section class="sheet card-back">
  <div class="identity">
    <p class="name">DANIEL HART</p>
    <p class="role">Business Manager</p>
  </div>
  <div class="divider"></div>
  <ul class="contact-list">
    <li class="phone"><svg class="icon"><use href="#i-phone"/></svg>(555) 214-0386</li>
    <li><svg class="icon"><use href="#i-mail"/></svg>info@crestmoreadvisory.net</li>
    <li><svg class="icon"><use href="#i-web"/></svg>www.crestmoreadvisory.net</li>
    <li><svg class="icon"><use href="#i-pin"/></svg><span>118 Harbor St Ste 9,<br>Portland, ME 04101, USA</span></li>
  </ul>
</section>

</body>
</html>
```